Letterhead Design Project

Consulting Company , we want a letterhead incorporating both the picture provided and the logo provided. The font name is monotype corsiva.
Target Market(s)
Dentist
Industry/Entity Type
Consulting
Font styles to use
Other font styles liked:
- monotype corsiva

Colors
0455a3
Requirements
Must have
- the logo, the picture (see attached), the website name, the email. and the phone numbers.
- Website: www.trquillarisadvisory.solutions
- Email: will be provided to the winner, please use placeholder
- Phone numbers:
- Petra Hallum 5829017763
- Owen Vrastik 6148250397

Nice to have
- a swoop or wave across the bottom. a line up the side. I don't know guys. design something unique and professional.

Should not have
- arrows pointing off the logo or anywhere. no arrows. our logo altered in anyway. no broken circles. no variences in blue. we like our logo the way it is. the font is monotype corsiva

```html
<!DOCTYPE html>
<html lang="en">
<head>
<meta charset="utf-8">
<title>Quillaris Advisory Letterhead</title>
<link rel="stylesheet" href="https://fonts.googleapis.com/css2?family=Cormorant+Garamond:ital,wght@1,500&family=PT+Sans&display=swap">
<style>
  :root {
    --brand-blue: #0455a3;
    --wave-blue: #1a7cc9;
    --wave-light: #2d9be0;
    --paper: #ffffff;
    --backdrop: #e4e4e4;
    --ink: #3a3a3a;
    --photo-dark: #4a4a4a;
    --photo-light: #bdbdbd;
  }
  * { margin: 0; padding: 0; box-sizing: border-box; }
  html, body { width: 1200px; height: 794px; overflow: hidden; }
  body { background: var(--backdrop); position: relative; }
  .letterhead {
    position: absolute; left: 330px; top: 17px;
    width: 540px; height: 760px;
    background: var(--paper);
    overflow: hidden;
    box-shadow: 0 4px 18px rgba(0,0,0,.18);
  }
  .brand {
    position: absolute; left: 40px; top: 34px;
    display: flex; align-items: center; gap: 10px;
  }
  .brand-dot {
    width: 30px; height: 30px; border-radius: 50%;
    border: 2px solid var(--brand-blue);
  }
  .brand-name {
    font-family: "Cormorant Garamond", serif;
    font-style: italic; font-weight: 500;
    font-size: 26px; color: var(--brand-blue);
  }
  .brand-address {
    position: absolute; left: 82px; top: 72px;
    font-family: "PT Sans", sans-serif;
    font-size: 8px; letter-spacing: .6px;
    color: var(--ink); text-transform: uppercase;
  }
  .footer-wave { position: absolute; left: 0; bottom: 0; width: 540px; height: 240px; }
  .contact {
    position: absolute; left: 36px; bottom: 26px;
    font-family: "PT Sans", sans-serif;
    font-size: 10.5px; line-height: 1.5; color: var(--paper);
  }
  .portrait {
    position: absolute; left: 300px; bottom: 58px;
    width: 100px; height: 100px; border-radius: 50%;
    border: 4px solid #e9e9e9;
    background: radial-gradient(circle at 50% 40%, var(--photo-light), var(--photo-dark));
  }
</style>
</head>
<body>
  <main class="letterhead">
    <header class="brand">
      <span class="brand-dot"></span>
      <span class="brand-name">Quillaris Advisory, LLC</span>
    </header>
    <p class="brand-address">412 Larkspur Lane, Alder Falls, Ohio 43077</p>

    <svg class="footer-wave" viewBox="0 0 540 240" aria-hidden="true">
      <path d="M0 40 C120 150 330 150 540 170 L540 240 L0 240 Z" fill="var(--wave-light)"/>
      <path d="M0 62 C130 165 330 160 540 185 L540 240 L0 240 Z" fill="var(--paper)"/>
      <path d="M0 72 C130 175 330 170 540 195 L540 240 L0 240 Z" fill="var(--wave-blue)"/>
      <path d="M0 95 C150 185 330 180 540 212" fill="none" stroke="var(--paper)" stroke-width="3"/>
      <path d="M0 110 C160 195 340 190 540 222" fill="none" stroke="var(--wave-light)" stroke-width="4"/>
    </svg>

    <div class="portrait" role="img" aria-label="Portrait photograph of the consultant"></div>

    <address class="contact">
      Petra Hallum &nbsp;5829017763<br>
      Owen Vrastik &nbsp;6148250397<br>
      info@trquillarisadvisory.solutions<br>
      www.trquillarisadvisory.solutions
    </address>
  </main>
</body>
</html>
```